Oven Cleaning flyer design

Hi there,
I need help designing a letterbox flyer. It needs to be DL size.
I have attached a rough design made with Chat GPT.
Would like back and front, have my business colors.
Please find attached mock up of what I would roughly like.
Also find attached logo.
Thank you

Target Market(s)

Home owners over 40

Industry/Entity Type

Cleaning

Requirements
Must have
• Logo, before after of oven, brand colors

```html
<!DOCTYPE html>
<html lang="en">
<head>
<meta charset="utf-8">
<title>Gleam Oven Care – Flyer</title>
<link href="https://fonts.googleapis.com/css2?family=Poppins:wght@400;600;700;800&display=swap" rel="stylesheet">
<style>
:root{
  --teal:#46c1cb;
  --teal-dark:#3bb3bd;
  --ink:#050505;
  --text:#3d3d3d;
  --paper:#ffffff;
  --mist:#eaf7fa;
}
*{margin:0;padding:0;box-sizing:border-box}
html,body{width:1200px;height:2545px;overflow:hidden;background:var(--paper)}
body{font-family:'Poppins',sans-serif;color:var(--ink)}
.flyer{position:relative;width:1200px;height:2545px;overflow:hidden;
  background:linear-gradient(180deg,var(--paper) 0,var(--paper) 1050px,var(--mist) 1100px,var(--paper) 1500px,var(--paper) 100%)}
.abs{position:absolute}

/* brand */
.brand{left:0;top:95px;width:1200px;display:flex;align-items:center;justify-content:center;gap:28px}
.brand-dot{width:110px;height:110px;border-radius:50%;background:var(--teal)}
.brand-name{font-weight:700;font-size:76px;color:var(--teal);letter-spacing:1px}

/* hero band */
.band{left:0;top:0}
.services-title{left:295px;top:387px;width:611px;height:108px;background:var(--ink);color:#fff;
  font-weight:600;font-size:82px;line-height:108px;text-align:center;letter-spacing:-1px;
  box-shadow:0 24px 22px -14px rgba(0,0,0,.45)}
.service{top:598px;width:280px;text-align:center}
.service-icon{display:block;margin:0 auto 24px}
.service-name{font-weight:700;font-size:38px;line-height:38px}
.service-kind{font-weight:400;font-size:39px;line-height:40px}

.seal{left:815px;top:905px}

/* why */
.why{left:86px;top:1215px}
.why-lead{font-weight:600;font-size:86px;line-height:86px;letter-spacing:-1px}
.why-name{font-weight:600;font-size:86px;line-height:90px;color:var(--teal);letter-spacing:-1px}
.about{left:86px;top:1425px;width:1010px;font-size:33.5px;line-height:53.5px;color:var(--text)}

.checks{left:92px;top:1765px;list-style:none}
.checks li{display:flex;align-items:center;gap:28px;height:100px}
.tick{width:54px;height:54px;flex:none}
.checks span{font-size:39px;line-height:39px;color:var(--text)}

.coupon{left:622px;top:1753px;width:471px;height:330px;border:3px dashed #555;border-radius:16px;text-align:center;padding-top:28px}
.coupon-amount{font-weight:700;font-size:96px;line-height:96px;letter-spacing:-3px;color:var(--ink)}
.coupon-line{font-weight:700;font-size:62px;line-height:64px;color:var(--teal);letter-spacing:-2px}
.coupon-big{font-weight:700;font-size:98px;line-height:84px;color:var(--teal);letter-spacing:-3px}
.coupon-note{font-size:26px;color:#333;margin-top:12px}

/* contact */
.contact{left:0;top:2196px;width:1200px;height:349px;background:var(--ink)}
.cta{left:123px;top:2140px;width:955px;height:90px;border-radius:45px;background:var(--teal);color:#fff;
  font-weight:700;font-size:42px;line-height:90px;text-align:center}
.phone{left:0;top:2255px;width:1200px;display:flex;align-items:center;justify-content:center;gap:36px}
.phone-badge{width:106px;height:106px}
.phone-number{font-weight:700;font-size:122px;line-height:122px;color:#fff;letter-spacing:-2px}
.site{left:0;top:2405px;width:1200px;text-align:center;font-size:50px;color:var(--teal);letter-spacing:4px}
</style>
</head>
<body>
<main class="flyer">

  <header class="brand abs">
    <span class="brand-dot"></span>
    <span class="brand-name">Gleam Oven Care</span>
  </header>

  <svg class="band abs" width="1200" height="1160" viewBox="0 0 1200 1160" aria-hidden="true">
    <path d="M0,1040 C300,1110 750,1080 1200,955 L1200,1080 C780,1050 360,1140 0,1060 Z" fill="var(--ink)"/>
    <path d="M0,297 H1200 V955 C750,1080 300,1110 0,1040 Z" fill="var(--teal)"/>
  </svg>

  <h2 class="services-title abs">Our Services</h2>

  <div class="service abs" style="left:44px">
    <svg class="service-icon" width="144" height="144" viewBox="0 0 144 144" role="img" aria-label="Oven icon">
      <path d="M72,3 A69,69 0 1,1 22,25" fill="none" stroke="var(--ink)" stroke-width="4"/>
      <path d="M22,25 A69,69 0 0,1 72,3" fill="none" stroke="#fff" stroke-width="4"/>
      <circle cx="72" cy="72" r="38" fill="var(--teal-dark)"/>
    </svg>
    <div class="service-name">Oven</div><div class="service-kind">Cleaning</div>
  </div>
  <div class="service abs" style="left:304px">
    <svg class="service-icon" width="144" height="144" viewBox="0 0 144 144" role="img" aria-label="Cooktop icon">
      <path d="M72,3 A69,69 0 1,1 22,25" fill="none" stroke="var(--ink)" stroke-width="4"/>
      <path d="M22,25 A69,69 0 0,1 72,3" fill="none" stroke="#fff" stroke-width="4"/>
      <circle cx="72" cy="72" r="38" fill="var(--teal-dark)"/>
    </svg>
    <div class="service-name">Cooktop</div><div class="service-kind">Cleaning</div>
  </div>
  <div class="service abs" style="left:589px">
    <svg class="service-icon" width="144" height="144" viewBox="0 0 144 144" role="img" aria-label="Rangehood icon">
      <path d="M72,3 A69,69 0 1,1 22,25" fill="none" stroke="var(--ink)" stroke-width="4"/>
      <path d="M22,25 A69,69 0 0,1 72,3" fill="none" stroke="#fff" stroke-width="4"/>
      <circle cx="72" cy="72" r="38" fill="var(--teal-dark)"/>
    </svg>
    <div class="service-name">Rangehood</div><div class="service-kind">Cleaning</div>
  </div>
  <div class="service abs" style="left:882px">
    <svg class="service-icon" width="144" height="144" viewBox="0 0 144 144" role="img" aria-label="Barbecue icon">
      <path d="M72,3 A69,69 0 1,1 22,25" fill="none" stroke="var(--ink)" stroke-width="4"/>
      <path d="M22,25 A69,69 0 0,1 72,3" fill="none" stroke="#fff" stroke-width="4"/>
      <circle cx="72" cy="72" r="38" fill="var(--teal-dark)"/>
    </svg>
    <div class="service-name">BBQ</div><div class="service-kind">Cleaning</div>
  </div>

  <svg class="seal abs" width="300" height="300" viewBox="0 0 300 300" role="img" aria-label="Satisfaction guarantee seal">
    <circle cx="150" cy="150" r="146" fill="var(--ink)"/>
    <circle cx="150" cy="150" r="112" fill="var(--teal)" stroke="#fff" stroke-width="4"/>
    <circle cx="150" cy="150" r="76" fill="var(--ink)"/>
  </svg>

  <section class="why abs">
    <div class="why-lead">Why Choose</div>
    <div class="why-name">Gleam Oven Care?</div>
  </section>

  <p class="about abs">We're a local family business providing professional, non-caustic oven cleaning across Sunshine Coast. Using specialized equipment and proven cleaning methods, we remove heavy grease, carbon build-up, smoke residue, restoring your oven safely and effectively.</p>

  <ul class="checks abs">
    <li><svg class="tick" viewBox="0 0 54 54" aria-hidden="true"><circle cx="27" cy="27" r="27" fill="var(--teal)"/><path d="M15,28 L24,37 L39,18" fill="none" stroke="#fff" stroke-width="4" stroke-linecap="round" stroke-linejoin="round"/></svg><span>Reliable<br>Service</span></li>
    <li><svg class="tick" viewBox="0 0 54 54" aria-hidden="true"><circle cx="27" cy="27" r="27" fill="var(--teal)"/><path d="M15,28 L24,37 L39,18" fill="none" stroke="#fff" stroke-width="4" stroke-linecap="round" stroke-linejoin="round"/></svg><span>Non-Caustic<br>Cleaning</span></li>
    <li><svg class="tick" viewBox="0 0 54 54" aria-hidden="true"><circle cx="27" cy="27" r="27" fill="var(--teal)"/><path d="M15,28 L24,37 L39,18" fill="none" stroke="#fff" stroke-width="4" stroke-linecap="round" stroke-linejoin="round"/></svg><span>Satisfaction<br>Guaranteed</span></li>
  </ul>

  <aside class="coupon abs">
    <div class="coupon-amount">$10 OFF</div>
    <div class="coupon-line">YOUR FIRST</div>
    <div class="coupon-big">CLEAN</div>
    <div class="coupon-note">When You Mention this flyer</div>
  </aside>

  <footer class="contact abs"></footer>
  <div class="cta abs">Call Now for Fast, Professional Service</div>
  <div class="phone abs">
    <svg class="phone-badge" viewBox="0 0 106 106" aria-hidden="true">
      <circle cx="53" cy="53" r="53" fill="var(--teal)"/>
      <path d="M38,28 C34,30 31,34 32,40 C35,56 48,70 64,75 C70,77 75,74 78,70 L72,62 C70,60 67,60 65,62 L61,65 C54,61 46,53 42,46 L45,42 C47,40 47,37 45,35 Z" fill="#fff"/>
    </svg>
    <span class="phone-number">0491 570 006</span>
  </div>
  <div class="site abs">www.gleamovencare.com.au</div>

</main>
</body>
</html>
```